Tidewell Electrical Solutions

On one side. LOGO (underneath:) Commercial Industrial Residential

- NAME & CONTACT DETAILS

Martin K. Oduya
Project Manager

(Cell icon) (441) 555-0187
(Email icon) twlelectricalsoultions@mailpost-demo.com
(Facebook & Instagram icons )@twlelectricalsolutions

Other side: LOGO - underneath ELECTRICAL CONSTRUCTION & MAINTENANCE . LED LIGHTING & AUTOMATION . LIFE SAFETY SYSTEMS (FIRE ALARM / SECURITY) . DATA & COMMUNICATION

```html
<!DOCTYPE html>
<html lang="en">
<head>
<meta charset="UTF-8">
<title>Tidewell Electrical Solutions – Business Card</title>
<link href="https://fonts.googleapis.com/css2?family=Montserrat:wght@500;600;700&family=Work+Sans:wght@400;500&display=swap" rel="stylesheet">
<style>
  :root {
    --teal: #0f566b;
    --teal-light: #1d6a80;
    --white: #ffffff;
    --ink-grey: #555b60;
    --rule-grey: #4a4a4a;
    --stage: #2b2c2e;
  }
  * { box-sizing: border-box; margin: 0; padding: 0; }
  html, body { width: 1200px; height: 900px; overflow: hidden; }
  body {
    background: var(--stage);
    position: relative;
    font-family: "Montserrat", sans-serif;
  }
  .card {
    position: absolute;
    left: 270px;
    width: 660px;
    height: 377px;
    border-radius: 20px;
    overflow: hidden;
  }
  /* ---------- Back side ---------- */
  .card-back {
    top: 50px;
    background: linear-gradient(120deg, var(--teal) 0%, var(--teal-light) 55%, var(--teal) 100%);
    color: var(--white);
  }
  .brand-back {
    position: absolute;
    top: 78px;
    left: 0;
    right: 0;
    text-align: center;
    font-family: "Montserrat", sans-serif;
    font-weight: 600;
    font-size: 30px;
    letter-spacing: 4px;
    line-height: 1.25;
    text-transform: uppercase;
    color: var(--white);
  }
  .services {
    position: absolute;
    top: 212px;
    left: 110px;
    list-style: none;
    font-weight: 600;
    font-size: 15px;
    letter-spacing: 1.4px;
    line-height: 1.55;
    text-transform: uppercase;
  }
  .services li::before {
    content: "";
    display: inline-block;
    width: 7px; height: 7px;
    border-radius: 50%;
    background: var(--white);
    margin: 0 14px 3px 0;
    vertical-align: middle;
  }
  /* ---------- Front side ---------- */
  .card-front {
    top: 473px;
    background: var(--white);
  }
  .brand-front {
    position: absolute;
    top: 40px;
    left: 46px;
    font-weight: 600;
    font-size: 17px;
    letter-spacing: 2.5px;
    line-height: 1.25;
    text-transform: uppercase;
    color: var(--teal);
  }
  .social {
    position: absolute;
    top: 66px;
    right: 40px;
    display: flex;
    align-items: center;
    gap: 10px;
    font-family: "Work Sans", sans-serif;
    font-size: 17px;
    letter-spacing: 0.4px;
    color: var(--ink-grey);
  }
  .social-mark {
    width: 20px; height: 20px;
    border-radius: 4px;
    background: var(--teal);
  }
  .name-tab {
    position: absolute;
    top: 150px;
    left: 0;
    width: 14px;
    height: 48px;
    background: var(--teal);
  }
  .person {
    position: absolute;
    top: 152px;
    left: 52px;
  }
  .person-name {
    font-weight: 700;
    font-size: 24px;
    letter-spacing: 1.2px;
    text-transform: uppercase;
    color: var(--teal);
  }
  .person-role {
    font-family: "Work Sans", sans-serif;
    font-size: 17px;
    color: var(--ink-grey);
    margin-top: 2px;
  }
  .contacts {
    position: absolute;
    top: 238px;
    left: 52px;
    list-style: none;
    font-family: "Work Sans", sans-serif;
    font-size: 17px;
    color: var(--ink-grey);
    line-height: 1.7;
  }
  .contacts li { display: flex; align-items: center; gap: 10px; }
  .contacts svg { width: 16px; height: 16px; flex: none; }
  .front-band {
    position: absolute;
    left: 0; bottom: 0;
    width: 660px; height: 377px;
    pointer-events: none;
  }
</style>
</head>
<body>

  <section class="card card-back">
    <h1 class="brand-back">Tidewell<br>Electrical<br>Solutions</h1>
    <ul class="services">
      <li>Data &amp; Communication</li>
      <li>LED Lighting &amp; Automation</li>
      <li>Electrical Construction &amp; Maintenance</li>
      <li>Life Safety Systems (Fire Alarm / Security)</li>
    </ul>
  </section>

  <section class="card card-front">
    <div class="brand-front">Tidewell<br>Electrical<br>Solutions</div>

    <div class="social">
      <span class="social-mark"></span>
      <span>@twlelectricalsolutions</span>
    </div>

    <div class="name-tab"></div>
    <div class="person">
      <div class="person-name">Martin K. Oduya</div>
      <div class="person-role">Project Manager</div>
    </div>

    <ul class="contacts">
      <li>
        <svg viewBox="0 0 16 16" aria-hidden="true"><path d="M4 1.5 L6.5 1.5 L7 5 L5.3 6 C6 8 7.8 9.8 10 10.7 L11 9 L14.5 9.5 L14.5 12 C14.5 13.5 13.5 14.5 12 14.5 C6.5 14 2 9.5 1.5 4 C1.5 2.5 2.5 1.5 4 1.5 Z" fill="none" stroke="#0f566b" stroke-width="1.4" stroke-linejoin="round"/></svg>
        (441) 555-0187
      </li>
      <li>
        <svg viewBox="0 0 16 16" aria-hidden="true"><rect x="1.5" y="3.5" width="13" height="9" rx="1" fill="none" stroke="#0f566b" stroke-width="1.4"/><path d="M1.8 4 L8 9 L14.2 4" fill="none" stroke="#0f566b" stroke-width="1.4"/></svg>
        twlelectricalsoultions@mailpost-demo.com
      </li>
    </ul>

    <svg class="front-band" viewBox="0 0 660 377" aria-hidden="true">
      <path d="M0 316 L388 350" stroke="#4a4a4a" stroke-width="6" fill="none"/>
      <path d="M0 326 L392 360 C406 361 412 346 432 346 L660 346 L660 377 L0 377 Z" fill="#0f566b"/>
    </svg>
  </section>

</body>
</html>
```